Website upgrade

I have two websites linked to the same business. One is for commercial and retail clients the other is for private and residential customers. I need a creative, modern thinking and bold designer to redesign my sites so that they look more professional and eye catching. The two sites are: www.peterhollandltd.com and www.brkfittingworks.com

Target Market(s)

brk fittings targets home owners and individuals who want work done to their property and peter holland targets commercial customers who want shopfitting work undertaken

Industry/Entity Type

Home Improvement

Number of Pages Required

5+ page

Font styles to use
Sans Serif

Colors
0255a3
3176b5
0292cd
85acd3
85cae6

Requirements
Must have
• i want a site to reflect my existing sites but with a bit more of a wow factor to draw customers in
Nice to have
• logo designed, video or slide show
Should not have
• blog page

```html
<!DOCTYPE html>
<html lang="en">
<head>
<meta charset="utf-8">
<title>Peter Holland Contracting</title>
<link href="https://fonts.googleapis.com/css2?family=Open+Sans:ital,wght@0,400;0,600;0,700;1,400&display=swap" rel="stylesheet">
<style>
:root{
  --navy:#0c3560;
  --navy-dark:#0a2c50;
  --brand:#0255a3;
  --brand-mid:#3176b5;
  --footer:#0560a8;
  --footer-base:#044f8e;
  --ink:#1d3c5e;
  --text:#555d66;
  --white:#ffffff;
  --light:#f4f6f8;
}
*{box-sizing:border-box;margin:0;padding:0}
html,body{width:1200px;height:2862px;overflow:hidden}
body{font-family:"Open Sans",Arial,sans-serif;color:var(--text);background:var(--white);position:relative}
a{color:inherit;text-decoration:none}

.site-header{height:80px;display:flex;align-items:center;justify-content:space-between;padding:0 100px 0 95px;background:var(--white)}
.brand{display:flex;align-items:center;gap:10px;background:#eef2f6;padding:6px 12px}
.brand-name{font-size:20px;font-weight:600;color:var(--ink);letter-spacing:.3px}
.main-nav{display:flex;gap:58px}
.main-nav a{font-size:12px;font-weight:700;color:#333;text-transform:uppercase;letter-spacing:.3px}

.hero{position:relative;height:467px;background:linear-gradient(100deg,#d9d3c8 0%,#c8bba8 35%,#b39e86 65%,#8d7762 100%)}
.hero-copy{position:absolute;left:660px;top:195px;color:var(--white)}
.hero-copy h1{font-size:42px;font-weight:700;line-height:1.05;text-transform:uppercase}
.hero-copy p{font-size:16px;margin-top:14px;width:440px;line-height:1.5}
.hero-dots{position:absolute;left:575px;bottom:26px;display:flex;gap:7px}
.hero-dots span{width:8px;height:8px;border-radius:50%;background:rgba(255,255,255,.5)}
.hero-dots span:first-child{background:var(--white)}

.welcome{height:308px;text-align:center;padding-top:62px}
.section-title{font-size:22px;font-weight:700;color:var(--ink);text-transform:uppercase}
.welcome p{width:870px;margin:24px auto 0;font-size:11.5px;line-height:26px}
.btn-solid{display:inline-block;margin-top:22px;background:var(--navy);color:var(--white);font-size:12px;font-weight:700;padding:13px 32px;border-radius:3px;text-transform:uppercase}

.split{display:flex;height:397px}
.split-photo{width:600px;height:100%;flex:none}
.split-panel{flex:1;background:var(--navy);color:var(--white);display:flex;flex-direction:column;justify-content:center;padding:0 100px}
.split-panel.align-right{text-align:right;align-items:flex-end}
.split-panel.align-left{padding:0 82px}
.split-panel h2{font-size:22px;font-weight:700;text-transform:uppercase}
.split-panel p{font-size:11.5px;line-height:24px;margin-top:18px;max-width:440px}
.btn-outline{display:inline-block;margin-top:22px;border:1px solid var(--white);border-radius:3px;color:var(--white);font-size:12px;padding:11px 30px;text-transform:uppercase}
.photo-kitchen{background:linear-gradient(135deg,#3a1c12 0%,#6b3520 40%,#b87a4a 70%,#5a2a18 100%)}
.photo-office{background:linear-gradient(120deg,#f1f1f0 0%,#d9d9d6 40%,#c32a25 42%,#b1221e 52%,#e3e3e0 54%,#c9c9c6 100%)}

.services{height:482px;text-align:center;padding-top:66px}
.services .subtitle{font-size:14px;margin-top:14px;color:#666}
.service-grid{display:flex;gap:31px;padding:0 100px;margin-top:28px;text-align:left}
.service-card{width:313px}
.service-photo{height:202px}
.service-card h3{font-size:16px;font-weight:700;color:var(--ink);margin-top:22px;text-transform:uppercase}
.service-card p{font-size:14px;margin-top:5px;color:#666}
.ph-kitchen{background:linear-gradient(135deg,#efefef,#7b3b2c 60%,#4e2418)}
.ph-site{background:linear-gradient(135deg,#5fb3e8,#d4ecf9 55%,#8cc8ef)}
.ph-office{background:linear-gradient(135deg,#c9d6e3,#f0f0f0 45%,#2a2f38 80%)}

.testimonials{position:relative;height:402px;background:linear-gradient(180deg,#2c3b4e,#1e2c3d);color:var(--white);text-align:center;padding-top:72px}
.testimonials .section-title{color:var(--white)}
.quote-row{display:flex;padding:0 100px;margin-top:38px;gap:80px;text-align:left}
.quote{display:flex;gap:30px;width:470px}
.avatar{width:112px;height:112px;border-radius:50%;flex:none;background:linear-gradient(135deg,#c9a58a,#7b5840);border:3px solid rgba(255,255,255,.25)}
.quote-body{position:relative;padding-top:4px}
.quote-body p{font-size:11.5px;font-style:italic;line-height:22px;width:290px}
.quote-name{font-size:11.5px;font-weight:700;margin-top:14px;text-transform:uppercase}
.quote-role{font-size:11px;font-style:italic;margin-top:2px}
.quote-dots{position:absolute;left:580px;bottom:70px;display:flex;gap:6px}
.quote-dots span{width:8px;height:8px;border-radius:50%;background:rgba(255,255,255,.35)}

.site-footer{height:268px;background:var(--footer);color:var(--white);display:flex;padding:38px 100px 0}
.footer-col{flex:none}
.footer-col h4{font-size:14px;font-weight:700;text-transform:uppercase;margin-bottom:18px}
.footer-col li{list-style:none;font-size:11.5px;line-height:26px;white-space:nowrap}
.col-about{width:376px}
.col-about p{font-size:11.5px;line-height:26px;width:340px}
.read-more{display:flex;align-items:center;gap:8px;font-size:11.5px;font-weight:600;margin-top:8px}
.col-welcome{width:185px}
.col-services{display:flex}
.col-services ul:first-child{width:284px}
.col-services ul:last-child{width:154px}

.footer-base{position:absolute;left:0;top:2800px;width:1200px;height:62px;background:var(--footer-base);color:var(--white);display:flex;align-items:center;justify-content:space-between;padding:0 100px;font-size:11.5px}
.social{display:flex;align-items:center;gap:16px}
.social i{width:12px;height:12px;border-radius:50%;background:var(--white);display:block}
</style>
</head>
<body>

<header class="site-header">
  <div class="brand"><span class="brand-name">Peter Holland Contracting Ltd</span></div>
  <nav class="main-nav">
    <a href="#">About</a><a href="#">Services</a><a href="#">Testimonials</a><a href="#">Quotes &amp; Estimates</a><a href="#">Contact</a>
  </nav>
</header>

<section class="hero" role="img" aria-label="Bright modern living room with armchair, cushions and television wall">
  <div class="hero-copy">
    <h1>Peter Holland<br>Contracting</h1>
    <p>One is for commercial and retail clients the other is for private and residential customers</p>
  </div>
  <div class="hero-dots"><span></span><span></span><span></span></div>
</section>

<section class="welcome">
  <h2 class="section-title">Welcome to Peter Holland Contracting</h2>
  <p>Peter Holland Contracting provide Project Management &amp; Interior fit-out services to all types of commercial &amp; retail clients. With over 25 years of industry experience, our attention to detail, focus on quality &amp; competitive pricing, ensures repeat business and continued growth with existing clients. If you would like any further information regarding the services that we provide, please do not hesitate to contact us</p>
  <a class="btn-solid" href="#">Call us now!</a>
</section>

<section class="split">
  <div class="split-photo photo-kitchen" role="img" aria-label="Luxury kitchen with dark wood cabinets and granite island"></div>
  <div class="split-panel align-right">
    <h2>Peter Holland Contracting</h2>
    <p>Peter Holland Contracting provide Project Management &amp; Interior fit-out services to all types of commercial &amp; retail clients. With over 25 years of industry experience, our attention to detail, focus on quality &amp; competitive pricing, ensures repeat business and continued growth with existing clients. If you would like any further information regarding the services that we provide, please do not hesitate to</p>
    <a class="btn-outline" href="#">Contact us</a>
  </div>
</section>

<section class="split">
  <div class="split-panel align-left">
    <h2>BRK Fittings</h2>
    <p>With over 25 years experience, BRK Fittings provide high-quality Joinery, carpentry &amp; property services throughout the Huddersfield area. Our primary trades are Joinery &amp; Carpentry, but we also specialise in Kitchen installation, Bathroom Installation, small building works and property refurbishments. We also undertake property maintenance and carryout...</p>
    <div><a class="btn-outline" href="#">Contact us</a></div>
  </div>
  <div class="split-photo photo-office" role="img" aria-label="Modern office interior with red feature wall and meeting table"></div>
</section>

<section class="services">
  <h2 class="section-title">What we do?</h2>
  <p class="subtitle">High quality interior fit-out &amp; refurbishment services</p>
  <div class="service-grid">
    <article class="service-card">
      <div class="service-photo ph-kitchen" role="img" aria-label="Fitted kitchen with wooden cabinets"></div>
      <h3>Property Services</h3>
      <p>Refurbishment, Maintenance &amp; Repairs</p>
    </article>
    <article class="service-card">
      <div class="service-photo ph-site" role="img" aria-label="Illustration of a room being painted and planned"></div>
      <h3>Site Services</h3>
      <p>Project &amp; Site Management</p>
    </article>
    <article class="service-card">
      <div class="service-photo ph-office" role="img" aria-label="Office manager at a desk on the phone"></div>
      <h3>Contracting (Sub-Contracting)</h3>
      <p>Shopfitting &amp; Installation Services</p>
    </article>
  </div>
</section>

<section class="testimonials" role="region" aria-label="Client testimonials">
  <h2 class="section-title">What our client's say</h2>
  <div class="quote-row">
    <div class="quote">
      <div class="avatar" role="img" aria-label="Client portrait"></div>
      <div class="quote-body">
        <p>Lorem Ipsum is simply dummy text of the printing and typesetting industry. Lorem Ipsum has been the industry's standard dummy text ever since...</p>
        <div class="quote-name">Marcus Bell</div>
        <div class="quote-role">Business man</div>
      </div>
    </div>
    <div class="quote">
      <div class="avatar" role="img" aria-label="Client portrait"></div>
      <div class="quote-body">
        <p>Lorem Ipsum is simply dummy text of the printing and typesetting industry. Lorem Ipsum has been the industry's standard dummy text ever since...</p>
        <div class="quote-name">Marcus Bell</div>
        <div class="quote-role">Business man</div>
      </div>
    </div>
  </div>
  <div class="quote-dots"><span></span><span></span><span></span></div>
</section>

<footer class="site-footer">
  <div class="footer-col col-about">
    <h4>Who we are?</h4>
    <p>Peter Holland Contracting provide Project Management &amp; Interior fit-out services to all types of commercial &amp; retail clients. With over 25 years of industry experience, our attention to detail, focus on quality &amp; competitive pricing...</p>
    <a class="read-more" href="#">Read more info
      <svg width="11" height="11" viewBox="0 0 11 11"><circle cx="5.5" cy="5.5" r="5.5" fill="#fff"/><path d="M4.5 3l2.5 2.5L4.5 8" stroke="#0560a8" stroke-width="1.5" fill="none"/></svg>
    </a>
  </div>
  <div class="footer-col col-welcome">
    <h4>Welcome</h4>
    <ul><li>Home</li><li>About</li><li>Services</li><li>Testimonials</li><li>Quotes &amp; Estimates</li><li>Contact</li></ul>
  </div>
  <div class="footer-col">
    <h4>Services</h4>
    <div class="col-services">
      <ul><li>Project Management</li><li>Project Planning</li><li>Roll-Out program management &amp; co-ordination</li><li>Design Management</li><li>Procurement/outsourcing</li><li>Site Management</li></ul>
      <ul><li>Site Supervision</li><li>Installation</li><li>Inspections &amp; Health &amp; Safety</li></ul>
    </div>
  </div>
</footer>

<div class="footer-base">
  <span>© 2016. Peter Holland Contracting Ltd. All rights reserved</span>
  <div class="social"><span>Connect with our social network :</span><i></i><i></i><i></i><i></i><i></i></div>
</div>

</body>
</html>
```